ROOFING SALES QUOTE TEMPLATE / BROCHURE

I am a roofing contractor looking to elevate and simplify the sales presentation of our roof installation services to our customers through a slick/company branded bid form or brochure. Im looking more for design elements in a template format that can be used/modified to have information populated based on unique customer needs.
I would like to have the bid form or brochure present 3 options to homeowners: GOOD / BETTER / BEST

Potentially include pages with details to educate the homeowners on the components of a roof, the material /product specifications included in each of the GOOD/BETTER/BEST options, our insurance information, licensing, etc.

For example: Homeowner Dalton is looking to have his asphalt shingle roof replaced on his residential home. Dalton knows nothing about roofing, but knows the roof is getting old.
Keelstone Roofing would like to present him with three replacement options, with different price points:
OPTION 1 (Good) = Remove and replace existing roof with new shingle tier 1 quality
OPTION 2 (BETTER) = remove and replace existing roof with new shingle tier 2 quality and better warranty
OPTION 3 (BEST) = remove and replace existing roof with new highest quality shingle and highest grade warranty

I would like one page to concisely present all three options, visually simple with price, and option summaries

One page which essentially educates on the components of a roof (attic space, trusses/rafters/eaves , plywood decking, roofing felts/underlayment, shingle material, metal flashings, ridge and hip shingles, ventilation, etc) -graphic?

One or more pages that show more specific details/scope of each of the options presented (unless this is TMI and we can provide a URL

Another page showcasing our license, insurance, bonds, certification, etc.

For branding, we are partnered with the manufacturer HMT in case we can co-brand anything.

Most of these will be used electronically and filled out as a PDF or similar.

Target Market(s)

Residential and commercial building owners looking for roof replacements

Industry/Entity Type

Roofing (USA - California)

Requirements
Must have
• present 3 options to homeowners: GOOD / BETTER / BEST -design must match logo colors
Nice to have
• One or more pages that show more specific details/scope of each of the options presented (unless this is TMI and we can provide a URL
Should not have
• too much wordiness

```html
<!DOCTYPE html>
<html lang="en">
<head>
<meta charset="utf-8">
<title>Keelstone Roofing – Brochure Pages</title>
<link href="https://fonts.googleapis.com/css2?family=Montserrat:wght@400;500;600;700;800&display=swap" rel="stylesheet">
<style>
:root{
  --stage:#58585a;
  --orange:#f26b36;
  --navy:#1b2a41;
  --brown:#6b5650;
  --olive:#6f7b3c;
  --slate:#33415a;
  --rust:#8a4a3f;
  --card:#f1f2f4;
  --white:#ffffff;
  --ink:#1e2b42;
}
*{box-sizing:border-box;margin:0;padding:0}
html,body{width:1200px;height:1200px;overflow:hidden}
body{background:var(--stage);font-family:"Montserrat",sans-serif;position:relative}
.page{position:absolute;width:369px;height:477px;background:var(--white);overflow:hidden}
.p1{left:36px;top:93px}.p2{left:416px;top:93px}.p3{left:796px;top:93px}
.p4{left:36px;top:631px}.p5{left:416px;top:631px}.p6{left:796px;top:631px}

.brand{display:flex;align-items:center;gap:8px;color:var(--orange);font-weight:800;line-height:1}
.brand-mark{width:12px;height:12px;background:var(--orange);flex:none}

.p1 .brand{position:absolute;left:0;right:0;top:170px;justify-content:center;font-size:28px;letter-spacing:1px}
.p1 .brand .brand-mark{width:20px;height:20px}
.intro-count{position:absolute;top:375px;width:100%;text-align:center;color:var(--orange);font-weight:700;font-size:28px}
.intro-title{position:absolute;top:410px;width:100%;text-align:center;color:var(--ink);font-weight:800;font-size:28px}

.cover-photo{position:absolute;inset:0;background:linear-gradient(180deg,#c9ccd2 0%,#8d939c 22%,#4b5261 45%,#26314a 70%,#1b2640 100%)}
.p2 .brand{position:absolute;left:18px;top:30px;font-size:13px}
.partner{position:absolute;right:19px;top:38px;color:var(--white);font-weight:800;font-size:20px;line-height:1}
.cover-title{position:absolute;top:238px;width:100%;text-align:center;color:var(--white);font-weight:800;font-size:24.5px;line-height:1.18}
.cover-tag{position:absolute;top:302px;width:100%;text-align:center;color:var(--white);font-size:16px;font-weight:400}
.client-frame{position:absolute;left:47px;top:354px;width:276px;height:74px;border:2px solid var(--white);padding:5px}
.client-box{background:var(--white);height:100%;padding:10px 13px;font-size:8.5px;font-weight:700;color:var(--ink);display:flex;flex-direction:column;gap:12px}
.site{position:absolute;width:100%;text-align:center;color:var(--white);font-size:11.5px;font-weight:400}
.p2 .site{top:443px}

.top-rule{position:absolute;top:0;left:0;right:0;height:6px;background:var(--orange)}
.options-title{position:absolute;top:36px;width:100%;text-align:center;color:var(--brown);font-weight:700;font-size:17.5px}
.tier{position:absolute;top:94px;width:97px;height:266px;background:var(--card);text-align:center}
.tier.good{left:35px}.tier.better{left:136px}.tier.best{left:237px}
.tier-head{height:56px;color:var(--white);font-weight:700;font-size:16px;padding-top:8px;position:relative}
.tier-head svg{position:absolute;left:0;bottom:-1px}
.good .tier-head{background:linear-gradient(180deg,#5c7a3f,#3e5a30)}
.better .tier-head{background:linear-gradient(180deg,#2f3d56,#1d2a40)}
.best .tier-head{background:linear-gradient(180deg,#8c4a3c,#6e3a30)}
.tier-icon{margin-top:10px;height:30px}
.tier-line{font-size:8.6px;line-height:1.25;padding:0 4px}
.tier-line.product{margin-top:9px;height:36px}
.tier-line.warranty{height:26px;border-bottom:1px solid #d5d6da;margin:0 4px;padding:3px 0 0;white-space:nowrap;font-size:8.1px}
.tier-line.parts{padding-top:10px}
.good .tier-line{color:var(--olive)}
.better .tier-line{color:#3b4760}
.best .tier-line{color:var(--rust)}
.tier-price{position:absolute;bottom:0;left:0;right:0;height:27px;color:var(--white);font-weight:700;font-size:14px;line-height:27px}
.good .tier-price{background:var(--olive)}.better .tier-price{background:var(--slate)}.best .tier-price{background:var(--rust)}
.foot{position:absolute;left:0;right:0;bottom:0;height:56px;background:linear-gradient(180deg,#24324a,#1a263b)}
.p3 .foot{height:57px}
.p3 .site{top:437px}

.anat-head{position:absolute;top:0;left:0;right:0;height:96px;background:var(--orange);color:var(--white);font-weight:700;font-size:18px;text-align:center;padding-top:31px;line-height:1.2}
.anat-art{position:absolute;left:98px;top:180px;width:140px;height:155px;background:linear-gradient(160deg,#5a6272 0%,#6d7482 40%,#d9b98c 70%,#c69263 100%);border-radius:6px}
.lab{position:absolute;color:var(--ink);font-size:7.6px;font-weight:700;line-height:1.1}
.lab small{display:block;font-size:5.6px;font-weight:500}
.leader{position:absolute;background:#333;height:.7px}
.orange-rule{position:absolute;left:0;right:0;bottom:56px;height:6px;background:var(--orange)}
.p4 .site,.p5 .site{top:443px}

.cred-photo{position:absolute;left:0;right:0;top:0;height:103px;background:linear-gradient(180deg,#4d5466 0%,#39425a 55%,#2a3550 100%)}
.cred-band{position:absolute;top:103px;left:0;right:0;height:28px;background:var(--navy);color:var(--white);font-weight:700;font-size:11px;text-align:center;line-height:28px}
.cred{position:absolute;top:210px;width:104px;text-align:center}
.cred.certified{left:27px}.cred.licensed{left:129px}.cred.insured{left:233px}
.cred-name{margin-top:8px;height:36px;font-size:7.3px;font-weight:700;color:var(--ink);line-height:1.15;display:flex;align-items:flex-end;justify-content:center}
.cred-text{margin-top:11px;font-size:7px;color:var(--ink);line-height:1.2}

.back-bar{position:absolute;top:0;left:0;right:0;height:11px;background:var(--navy)}
.p6 .brand{position:absolute;left:0;right:0;top:150px;justify-content:center;font-size:28px}
.p6 .brand .brand-mark{width:20px;height:20px}
.back-rule{position:absolute;top:325px;left:0;right:0;height:5px;background:var(--orange)}
.back-foot{position:absolute;top:330px;left:0;right:0;bottom:0;background:linear-gradient(180deg,#1f2c43,#1a263b)}
.contact{position:absolute;left:33px;display:flex;align-items:center;gap:8px;color:var(--white);font-size:7px;font-weight:700;line-height:1.2}
.contact svg{flex:none}
.guarantee{position:absolute;left:219px;top:357px;width:116px;text-align:center;color:var(--white);font-weight:700;font-size:13px}
.pill{position:absolute;left:219px;width:116px;height:18px;color:var(--white);font-weight:700;font-size:10px;text-align:center;line-height:18px}
.pill.comm{top:380px;background:var(--orange)}
.pill.open{top:408px;background:var(--brown)}
.pill.hon{top:436px;background:var(--olive)}
</style>
</head>
<body>

<section class="page p1">
  <div class="brand"><span class="brand-mark"></span><span>KEELSTONE<br>ROOFING</span></div>
  <div class="intro-count">5 PAGES</div>
  <div class="intro-title">BROCURE DESIGN</div>
</section>

<section class="page p2">
  <div class="cover-photo" role="img" aria-label="Photo of a two-storey house with a dark shingle roof under an overcast sky"></div>
  <div class="brand"><span class="brand-mark"></span><span>KEELSTONE<br>ROOFING</span></div>
  <div class="partner">HMT</div>
  <h1 class="cover-title">ROOF REPLACEMENT<br>PROPOSAL</h1>
  <p class="cover-tag">Built to last. Backed by excellence</p>
  <div class="client-frame"><div class="client-box"><span>CLIENT NAME :</span><span>ADDRESS :</span></div></div>
  <p class="site">www.keelstoneroofer.com</p>
</section>

<section class="page p3">
  <div class="top-rule"></div>
  <h2 class="options-title">ROOF REPLACEMENT OPTION</h2>

  <div class="tier good">
    <div class="tier-head">GOOD<svg width="97" height="14" viewBox="0 0 97 14"><path d="M0 8 Q12 0 24 6 T48 6 T72 6 T97 5 V14 H0Z" fill="#f1f2f4"/></svg></div>
    <div class="tier-icon"><svg width="30" height="30" viewBox="0 0 30 30"><circle cx="15" cy="15" r="13" fill="none" stroke="#6f7b3c" stroke-width="2"/><circle cx="15" cy="15" r="9" fill="#6f7b3c"/><path d="M10 14h3v6h-3zM14 20v-6l3-5c1 0 2 1 1.5 2.5L18 14h3c1 0 1.5 1 1 2l-2 4z" fill="#fff"/></svg></div>
    <p class="tier-line product">Tier 1<br>Shingles</p>
    <p class="tier-line warranty">Basic Warranty</p>
    <p class="tier-line parts">Essential<br>Components</p>
    <div class="tier-price">$0</div>
  </div>

  <div class="tier better">
    <div class="tier-head">BETTER<svg width="97" height="14" viewBox="0 0 97 14"><path d="M0 5 Q12 10 24 5 T48 6 T72 4 T97 7 V14 H0Z" fill="#f1f2f4"/></svg></div>
    <div class="tier-icon"><svg width="30" height="30" viewBox="0 0 30 30"><path d="M15 2 L26 6 V14 C26 21 21 26 15 28 C9 26 4 21 4 14 V6Z" fill="#33415a"/><path d="M15 6 L22 8.5 V14 C22 18.5 19 22 15 23.5 C11 22 8 18.5 8 14 V8.5Z" fill="#fff"/><path d="M11 14.5 l3 3 l5 -6" stroke="#33415a" stroke-width="2.2" fill="none"/></svg></div>
    <p class="tier-line product">Tier 2<br>Shingles</p>
    <p class="tier-line warranty">Extended Warranty</p>
    <p class="tier-line parts">Enhanced<br>Materials</p>
    <div class="tier-price">$00</div>
  </div>

  <div class="tier best">
    <div class="tier-head">BEST<svg width="97" height="14" viewBox="0 0 97 14"><path d="M0 6 Q12 2 24 7 T48 5 T72 8 T97 4 V14 H0Z" fill="#f1f2f4"/></svg></div>
    <div class="tier-icon"><svg width="30" height="30" viewBox="0 0 30 30"><circle cx="15" cy="15" r="13" fill="#8a4a3f"/><circle cx="15" cy="15" r="8.5" fill="none" stroke="#fff" stroke-width="1.8"/><path d="M15 10.5l1.4 2.9 3.1.4-2.3 2.2.6 3.1-2.8-1.5-2.8 1.5.6-3.1-2.3-2.2 3.1-.4z" fill="#fff"/></svg></div>
    <p class="tier-line product" style="margin-top:4px;height:41px">Premium<br>Architectural<br>Shingles</p>
    <p class="tier-line warranty">Lifetime Warranty</p>
    <p class="tier-line parts">Best Durability +<br>Performance</p>
    <div class="tier-price">$000</div>
  </div>

  <div class="foot"></div>
  <p class="site">www.keelstoneroofer.com</p>
</section>

<section class="page p4">
  <h2 class="anat-head">ANATOMY OF A MODERN<br>ROOFING SYSTEM</h2>
  <div class="anat-art" role="img" aria-label="Exploded illustration of roof layers: shingles, underlayment, plywood decking and rafters"></div>

  <div class="lab" style="left:20px;top:179px">SHINGLES<small>PROTECTIVE AND<br>DECORATIVE TOP LAYER</small></div>
  <div class="leader" style="left:66px;top:183px;width:60px"></div>
  <div class="lab" style="left:20px;top:228px">UNDERLAYMENT<small>WATERPROOF<br>PROTECTIVE BARRIER</small></div>
  <div class="leader" style="left:90px;top:232px;width:22px"></div>
  <div class="lab" style="left:20px;top:285px">DECKING<small>PLYWOOD BASE LAYER</small></div>
  <div class="leader" style="left:64px;top:289px;width:88px"></div>
  <div class="lab" style="left:19px;top:328px">TRUSSES/RAFTERS<small>FRAMEWORK THAT SUPPORTS THE ROOF</small></div>
  <div class="leader" style="left:104px;top:332px;width:28px"></div>

  <div class="lab" style="left:241px;top:196px">RIDGE CAPS<small>PROTECTS ROOF PEAKS</small></div>
  <div class="leader" style="left:220px;top:200px;width:19px"></div>
  <div class="lab" style="left:241px;top:233px">VENTILATION<small>ALLOWS AIRFLOW, PREVENTS HEAT<br>&amp; MOISTURE BUILDUP</small></div>
  <div class="leader" style="left:226px;top:237px;width:13px"></div>
  <div class="lab" style="left:241px;top:272px">FLASHING<small>SEALS ROOF EDGES &amp; PENETRATIONS</small></div>
  <div class="leader" style="left:214px;top:276px;width:25px"></div>

  <div class="orange-rule"></div>
  <div class="foot"></div>
  <p class="site">www.keelstoneroofer.com</p>
</section>

<section class="page p5">
  <div class="cred-photo" role="img" aria-label="Photo of a house gable with a dark shingle roof and skylight"></div>
  <h2 class="cred-band">OUR CREDENTIALS</h2>

  <div class="cred certified">
    <svg width="56" height="56" viewBox="0 0 56 56"><circle cx="28" cy="28" r="26" fill="#fff" stroke="#c62b2b" stroke-width="3"/><circle cx="28" cy="28" r="12" fill="#c62b2b"/><path d="M28 21l2 4.3 4.6.6-3.3 3.2.8 4.6-4.1-2.2-4.1 2.2.8-4.6-3.3-3.2 4.6-.6z" fill="#fff"/></svg>
    <div class="cred-name">HMT CERTIFIED<br>CONTRACTOR</div>
    <p class="cred-text">Highest level<br>of certification<br>in the industry</p>
  </div>
  <div class="cred licensed">
    <svg width="56" height="56" viewBox="0 0 56 56"><circle cx="28" cy="28" r="26" fill="#fff" stroke="#e0782e" stroke-width="3"/><rect x="18" y="16" width="20" height="24" rx="2" fill="#e0782e"/><circle cx="31" cy="35" r="7" fill="#fff" stroke="#e0782e" stroke-width="2"/><path d="M27.5 35l2.5 2.5 4-4.5" stroke="#e0782e" stroke-width="2" fill="none"/></svg>
    <div class="cred-name">LICENSED<br>CONTRACTOR<br>#1048213</div>
    <p class="cred-text">Legal and<br>operational<br>compliance</p>
  </div>
  <div class="cred insured">
    <svg width="56" height="56" viewBox="0 0 56 56"><circle cx="28" cy="28" r="26" fill="#fff" stroke="#7fb0d4" stroke-width="3"/><path d="M28 13 L40 17 V27 C40 35 34 40 28 43 C22 40 16 35 16 27 V17Z" fill="#7fb0d4"/><path d="M22 28l4.5 4.5 8-8.5" stroke="#fff" stroke-width="3" fill="none"/></svg>
    <div class="cred-name">FULLY<br>INSURED<br>&amp; BONDED</div>
    <p class="cred-text">Protection for both<br>the company and<br>the homeowner</p>
  </div>

  <div class="orange-rule"></div>
  <div class="foot"></div>
  <p class="site">www.keelstoneroofer.com</p>
</section>

<section class="page p6">
  <div class="back-bar"></div>
  <div class="brand"><span class="brand-mark"></span><span>KEELSTONE<br>ROOFING</span></div>
  <div class="back-rule"></div>
  <div class="back-foot"></div>

  <div class="contact" style="top:357px">
    <svg width="19" height="19" viewBox="0 0 20 20"><circle cx="10" cy="10" r="9" fill="none" stroke="#fff" stroke-width="1.3"/><path d="M7 5.5l1.5 2.5-1 1.2c.6 1.4 1.6 2.4 3 3l1.2-1 2.5 1.5-.7 1.8c-3.8 0-7.3-3.5-7.3-7.3z" fill="#fff"/></svg>
    <span>+1 619-555-0148</span></div>
  <div class="contact" style="top:383px">
    <svg width="19" height="19" viewBox="0 0 20 20"><circle cx="10" cy="10" r="9" fill="none" stroke="#fff" stroke-width="1.3"/><rect x="5.5" y="7" width="9" height="6.5" fill="none" stroke="#fff" stroke-width="1.1"/><path d="M5.5 7l4.5 3.5L14.5 7" fill="none" stroke="#fff" stroke-width="1.1"/></svg>
    <span>info@keelstoneroofer.com</span></div>
  <div class="contact" style="top:409px">
    <svg width="19" height="19" viewBox="0 0 20 20"><circle cx="10" cy="10" r="9" fill="none" stroke="#fff" stroke-width="1.3"/><path d="M10 15s-3.5-3.7-3.5-6.2a3.5 3.5 0 017 0C13.5 11.3 10 15 10 15z" fill="#fff"/><circle cx="10" cy="8.8" r="1.3" fill="#1f2c43"/></svg>
    <span>4820 Harbor View Drive, #210,<br>San Diego, CA 92101</span></div>
  <div class="contact" style="top:435px">
    <svg width="19" height="19" viewBox="0 0 20 20"><circle cx="10" cy="10" r="9" fill="none" stroke="#fff" stroke-width="1.3"/><circle cx="10" cy="10" r="5" fill="none" stroke="#fff" stroke-width="1"/><ellipse cx="10" cy="10" rx="2.2" ry="5" fill="none" stroke="#fff" stroke-width="1"/><path d="M5 10h10" stroke="#fff" stroke-width="1"/></svg>
    <span>www.keelstoneroofer.com</span></div>

  <div class="guarantee">WE GUARANTEE</div>
  <div class="pill comm">COMMUNICATION</div>
  <div class="pill open">OPENNESS</div>
  <div class="pill hon">HONESTY</div>
</section>

</body>
</html>
```